Optometrist/Eye Care Clinic Business card with new logo attached

We are a small, independent eye care clinic in Canada. We have recently updated our logo (as attached), and would like a professional, modern and health care oriented business card to highlight our office details and our optometrist. We'd like to incorporate the blue colours as seen on our logo.

Target Market(s)

demographic: age 35-65 male/female equal

Industry/Entity Type

Health Care

Contact Information for Business Card

Name of clinic: "Marrow Bend Eye Care Optometry"

Font styles to use
Sans Serif

Colors
0355a3

Requirements
Must have
• our website: marrowbendeyecare.com
• Dr Lena Quorvik
• Optometrist
• 217-392 E Halvering Ave
• Vancouver BC V6R 3J8
• P: 604-319-2058
• E: info@marrowbendeyecare.com
Nice to have
• front side: logo/name of clinic as seen on logo attached and website
• backside: logo on the left side, and name/title/address/phone/email

```html
<!DOCTYPE html>
<html lang="en">
<head>
<meta charset="utf-8">
<title>Marrow Bend Eye Care Optometry – Business Card</title>
<link rel="stylesheet" href="https://fonts.googleapis.com/css2?family=Arimo:wght@400;700&family=Questrial&display=swap">
<style>
  :root {
    --backdrop: #c4c4c4;
    --card-white: #f6f6f6;
    --navy: #0d3c5e;
    --sky: #2aa0c8;
    --band-dark: #0b3a55;
    --band-light: #1a87b2;
    --stripe: #3aa9d2;
    --brand-blue: #1d5f8e;
    --ink-grey: #444444;
    --white: #ffffff;
  }
  * { margin: 0; padding: 0; box-sizing: border-box; }
  html, body {
    width: 1200px;
    height: 960px;
    overflow: hidden;
    background: var(--backdrop);
    font-family: "Arimo", Arial, sans-serif;
  }
  .card {
    position: absolute;
    width: 600px;
    height: 342px;
    border-radius: 16px;
    background: var(--card-white);
    overflow: hidden;
  }
  .card--front { left: 322px; top: 108px; }
  .card--back  { left: 320px; top: 493px; }

  .front__website {
    position: absolute;
    right: 37px;
    top: 290px;
    font-size: 14px;
    color: var(--ink-grey);
  }

  .back__wave {
    position: absolute;
    inset: 0;
    width: 600px;
    height: 342px;
  }
  .back__person {
    position: absolute;
    left: 40px;
    top: 50px;
  }
  .person__name {
    font-size: 22px;
    font-weight: 700;
    color: var(--navy);
    line-height: 26px;
  }
  .person__title {
    font-size: 15px;
    color: var(--sky);
    line-height: 18px;
  }
  .brand {
    position: absolute;
    left: 377px;
    top: 32px;
    width: 160px;
    display: flex;
    flex-direction: column;
    align-items: center;
  }
  .brand__dot {
    width: 78px;
    height: 78px;
    border-radius: 50%;
    background: var(--brand-blue);
    margin-bottom: 26px;
  }
  .brand__name {
    font-family: "Questrial", Arial, sans-serif;
    font-size: 17px;
    line-height: 21px;
    letter-spacing: 2.5px;
    text-transform: uppercase;
    text-align: center;
    color: var(--brand-blue);
  }
  .back__contact {
    position: absolute;
    left: 40px;
    top: 230px;
    font-size: 14px;
    line-height: 18px;
    color: var(--white);
  }
  .contact__address { margin-bottom: 18px; }
  .back__website {
    position: absolute;
    right: 45px;
    top: 303px;
    font-size: 14px;
    color: var(--white);
  }
</style>
</head>
<body>
  <section class="card card--front">
    <p class="front__website">www.marrowbendeyecare.com</p>
  </section>

  <section class="card card--back">
    <svg class="back__wave" viewBox="0 0 600 342" aria-hidden="true">
      <defs>
        <linearGradient id="band-gradient" x1="0" y1="0" x2="1" y2="0">
          <stop offset="0" stop-color="var(--band-dark)"/>
          <stop offset="1" stop-color="var(--band-light)"/>
        </linearGradient>
        <linearGradient id="stripe-gradient" x1="0" y1="0" x2="1" y2="0">
          <stop offset="0" stop-color="var(--stripe)"/>
          <stop offset="1" stop-color="var(--stripe)" stop-opacity="0.2"/>
        </linearGradient>
      </defs>
      <path d="M0,139 C110,122 205,150 268,202 C195,160 105,150 0,160 Z" fill="url(#stripe-gradient)"/>
      <path d="M0,167 C150,140 300,258 430,252 C510,248 560,212 600,178 L600,342 L0,342 Z" fill="url(#band-gradient)"/>
    </svg>

    <div class="back__person">
      <h1 class="person__name">Dr Lena Quorvik</h1>
      <p class="person__title">Optometrist</p>
    </div>

    <div class="brand">
      <span class="brand__dot"></span>
      <p class="brand__name">Marrow Bend<br>Eye Care<br>Optometry</p>
    </div>

    <div class="back__contact">
      <p class="contact__address">217-392 E Halvering Ave<br>Vancouver BC V6R 3J8</p>
      <p class="contact__lines">604-319-2058<br>info@marrowbendeyecare.com</p>
    </div>
    <p class="back__website">www.marrowbendeyecare.com</p>
  </section>
</body>
</html>
```